Consulting company, design, Interior design in commercial real estate (Tertiai sector *

Company name: VORANDEL: from the Greek Evexia well-being, was born from a desire to combine well-being and work. By the choice of design, materials, design and furniture, everything is thought from this perspective

Logo: Essay with Möbius Ribbon and / or with the infinite acronym / and or triangle ...
Sentences to write:
"The exclusive partner for your development projects"
"Consulting - Design - Construction"
"We manage EVERYTHING for you"

On the back: Photo (attached; if photo is not clear, another photo can be provided) with company name and "VORANDEL, Excellence and reliability"
My name / First name: provided later (double name), Manager
Address: supplied later
Tel: supplied later
Website: www. vorandel.com
Colors: Black, gold and white. Other admissible colors
See attached files

Real estate business

Nom de l'entreprise : VORANDEL : du grec Evexia bien être, est né d'une volonté de faire rimer bien être et travail. Par le choix de la conception, des matériaux, du design et du mobilier, tout est pensé dans cette optique

Logo : Essai avec Ruban de Möbius et /ou avec le sigle infini / et ou triangle...
Phrases à inscrire :
"Le partenaire exclusif de vos projets d'aménagement"
"Conseil - Conception - Construction"
"Nous gérons TOUT pour vous"

Au verso : Photo (ci-jointe ; si photo pas nette, une autre photo peut être fournie) avec nom de l'entreprise et Mention "VORANDEL, Excellence et fiabilité"
Mon nom / Prénom : fourni ultérieurement (prénom double), Gérant
Adresse : fourni ultérieurement
Tél : fourni ultérieurement
Site Web : www. vorandel.com
Couleurs : Noir, doré et blanc. Autre couleurs recevables
Voir fichiers ci-joint

• My project must be simple, clear, neat and design.
The business card must catch the customer

```html
<!DOCTYPE html>
<html lang="en">
<head>
<meta charset="utf-8">
<title>Vorandel Business Card</title>
<link href="https://fonts.googleapis.com/css2?family=Montserrat:wght@400;500;700&display=swap" rel="stylesheet">
<style>
  :root {
    --page: #ffffff;
    --card: #1f2223;
    --gold: #d9a62b;
    --gold-deep: #a57c1f;
    --white: #ffffff;
    --photo-a: #6b5a4e;
    --photo-b: #2b2b2e;
  }
  * { margin: 0; padding: 0; box-sizing: border-box; }
  html, body {
    width: 960px; height: 1200px; overflow: hidden;
    background: var(--page);
    font-family: "Montserrat", sans-serif;
  }
  .card {
    position: absolute; left: 174px; width: 612px; height: 351px;
    background: var(--card); overflow: hidden;
  }
  .card--front { top: 175px; }
  .card--back { top: 674px; }

  .stripe-band {
    position: absolute; left: 0; right: 0; bottom: 0; height: 22px;
    background: linear-gradient(90deg, var(--gold), var(--gold-deep) 50%, var(--gold));
  }
  .photo-band {
    position: absolute; left: 0; top: 31px; width: 142px; height: 103px;
    border-radius: 0 52px 52px 0;
    background: linear-gradient(90deg, var(--gold-deep), var(--gold));
  }
  .portrait {
    position: absolute; left: 38px; top: 32px; width: 102px; height: 102px;
    border-radius: 50%; border: 3px solid var(--gold);
    background: radial-gradient(circle at 50% 40%, var(--photo-a), var(--photo-b));
  }

  .person {
    position: absolute; right: 30px; top: 50px; text-align: right;
  }
  .person__name {
    font-size: 29px; font-weight: 700; color: var(--white); letter-spacing: -0.5px;
    line-height: 1;
  }
  .person__name span { color: var(--gold); }
  .person__rule {
    position: absolute; left: 414px; right: 0; top: 86px; height: 2px; background: var(--gold);
  }
  .person__role {
    position: absolute; right: 30px; top: 92px;
    font-size: 21px; font-weight: 400; color: var(--white);
  }

  .wordmark {
    position: absolute; color: var(--gold); font-weight: 400;
    letter-spacing: 6px; line-height: 1; white-space: nowrap;
    transform: translateX(-50%);
  }
  .card--front .wordmark { left: 174px; top: 196px; font-size: 38px; }
  .card--back .wordmark { left: 424px; top: 82px; font-size: 38px; }

  .contacts { position: absolute; left: 383px; top: 168px; list-style: none; }
  .contacts li {
    display: flex; align-items: center; height: 35px;
    font-size: 13px; color: var(--white);
  }
  .contacts svg { width: 18px; height: 18px; margin-right: 13px; flex: none; }

  .claims { position: absolute; left: 76px; top: 190px; list-style: none; }
  .claims li {
    display: flex; align-items: center; height: 33px;
    font-size: 14px; color: var(--white);
  }
  .claims svg { width: 14px; height: 14px; margin-right: 19px; }
</style>
</head>
<body>

<section class="card card--front">
  <div class="photo-band" role="img" aria-label="Gold diagonal stripe band"></div>
  <div class="portrait" role="img" aria-label="Portrait photo of the manager"></div>

  <div class="person">
    <p class="person__name"><span>YOUR</span> NAME</p>
  </div>
  <div class="person__rule"></div>
  <p class="person__role">Manager</p>

  <p class="wordmark">VORANDEL</p>

  <ul class="contacts">
    <li>
      <svg viewBox="0 0 20 20" aria-hidden="true"><path fill="#d9a62b" d="M5 2l3 4-2 2c1 2 3 4 5 5l2-2 4 3-2 3C9 17 3 11 2 4z"/></svg>
      000-1234-5678
    </li>
    <li>
      <svg viewBox="0 0 20 20" aria-hidden="true"><path fill="#d9a62b" d="M10 1a6 6 0 0 0-6 6c0 5 6 12 6 12s6-7 6-12a6 6 0 0 0-6-6zm0 8.5a2.5 2.5 0 1 1 0-5 2.5 2.5 0 0 1 0 5z"/></svg>
      87 Alder Court&nbsp; MI 48390
    </li>
    <li>
      <svg viewBox="0 0 20 20" aria-hidden="true"><rect x="2" y="5" width="16" height="11" fill="#d9a62b"/><path d="M2 5l8 6 8-6" fill="none" stroke="#1f2223" stroke-width="1.4"/></svg>
      contact@vorandel.com
    </li>
    <li>
      <svg viewBox="0 0 20 20" aria-hidden="true"><circle cx="10" cy="10" r="8" fill="#d9a62b"/><path d="M2 10h16M10 2c-4 4-4 12 0 16M10 2c4 4 4 12 0 16" fill="none" stroke="#1f2223" stroke-width="1"/></svg>
      www.vorandel.com
    </li>
  </ul>

  <div class="stripe-band" role="img" aria-label="Gold diagonal stripe band"></div>
</section>

<section class="card card--back">
  <p class="wordmark">VORANDEL</p>

  <ul class="claims">
    <li><svg viewBox="0 0 14 14" aria-hidden="true"><path d="M3 2l6 5-6 5" fill="none" stroke="#d9a62b" stroke-width="2.4"/></svg>The exclusive partner for you development projects</li>
    <li><svg viewBox="0 0 14 14" aria-hidden="true"><path d="M3 2l6 5-6 5" fill="none" stroke="#d9a62b" stroke-width="2.4"/></svg>Consulting - Design - Construction</li>
    <li><svg viewBox="0 0 14 14" aria-hidden="true"><path d="M3 2l6 5-6 5" fill="none" stroke="#d9a62b" stroke-width="2.4"/></svg>We manage EVERYTHING for you</li>
  </ul>

  <div class="stripe-band" role="img" aria-label="Gold diagonal stripe band"></div>
</section>

</body>
</html>
```